CSS design for a web application

We are currently building a web application in JAVA. The application uses a combination of a HTML template and CSS for the look and feel. We currenly have a very corporate look and feel for demo puposes, but we need to have some CSS designs that we can show to prospective customers. One of the functionalities of our application is the possibility to upload a customer's own (CSS) design in the application.

Our first customer is a high school in The Netherlands (12-18 year students) for children who are physically challenged. So the design should be easy to read, buttons should be easy to see, read and click and the different parts/texts on the website shouldn't be too close together. At the same time, we would like to avoid too much scrolling (especially horizontally). Go with a minimun screen resolution of 1024 x 768.

As our users are children, nice colours and other fun elements would be nice, while keeping a 'school like' appearance. Please use pictures and icons that our users will relate too. We want to communicate that our software is easy, fun and at the same time professional.

Our product is based on Tarvo Apps by Tarvo and thus Tarvo applications as Pluxo, Calendar, Tarvo Docs etc are all integrated in our software solution.

Find attached a static HTML file that contains our current CSS design. This should be used as a basis as it contains al the CSS elements that are used in the application. Please note that jQuery (javascript) knowledge is necessary.

Target Market(s)

Students at high school (age group 12/13 to 17/18). Users have physical disabilities that sometimes means they need special equipment/tools to operate their laptop.

Requirements
Must have
• Easy too navigate, buttons that are easy to see/use
Nice to have
• 'WOW' factor when people look at the design
Should not have
• buttons/text that is too small, too close together

```html
<!DOCTYPE html>
<html lang="nl">
<head>
<meta charset="utf-8">
<title>Study Guide Engels – Brightnest</title>
<link rel="stylesheet" href="https://fonts.googleapis.com/css2?family=Arimo:wght@400;700&family=Roboto+Condensed:wght@700&display=swap">
<style>
:root{
  --top-dark:#0f5c94;
  --top-light:#2a8fd0;
  --header-light:#f4f4f4;
  --header-dark:#c9c9c9;
  --main-blue:#1e90d4;
  --main-blue-light:#4fb3ea;
  --panel-blue:#7fcdf0;
  --panel-edge:#5bbce8;
  --menu-btn-top:#5cc6f4;
  --menu-btn-bottom:#1a9ae0;
  --sub-btn-top:#eef3e6;
  --sub-btn-bottom:#cfd8c3;
  --red-top:#c8120c;
  --red-bottom:#8e0a06;
  --orange:#ff6a13;
  --link:#1b8fd3;
  --deadline:#e0140a;
  --ink:#111;
  --white:#fff;
  --footer:#3d4446;
  --footer-dark:#2d3234;
  --brand:#2b2f33;
  --brand-soft:#54606a;
  --row-a:#c4e4f5;
  --row-b:#cfd0e0;
}
*{box-sizing:border-box;margin:0;padding:0}
html,body{width:1200px;height:770px;overflow:hidden}
body{font-family:"Arimo",Arial,sans-serif;background:var(--white);position:relative}

.topbar{position:absolute;left:0;top:0;width:1200px;height:90px;background:linear-gradient(var(--top-light),var(--top-dark))}
.app{position:absolute;top:12px;transform:translateX(-50%);display:flex;flex-direction:column;align-items:center;color:var(--white);font-weight:700;font-size:14px;white-space:nowrap}
.app svg{width:38px;height:38px;margin-bottom:6px}
.app.mail{left:57px}
.app.calendar{left:128px}
.app.docs{left:218px}
.app.sites{left:295px}
.app.chat{left:349px}
.welcome{position:absolute;left:779px;top:15px;color:var(--white);font-weight:700;font-size:16px}
.welcome span{color:#7fe3ff}

.header{position:absolute;left:0;top:90px;width:1200px;height:138px;background:linear-gradient(var(--header-light),var(--header-dark));border-top:2px solid #0b4e80}
.brand{position:absolute;left:36px;top:36px;display:flex;align-items:center;gap:10px;font-weight:700;font-size:32px;color:var(--brand)}
.brand i{width:28px;height:28px;border-radius:50%;background:var(--link);display:block}

.tools{position:absolute;left:766px;top:46px;width:424px;height:132px;border-radius:8px;overflow:hidden;box-shadow:0 2px 4px rgba(0,0,0,.3)}
.tools-row{height:80px;background:linear-gradient(var(--red-top),var(--red-bottom));display:flex;justify-content:space-around;align-items:center}
.tool{display:flex;flex-direction:column;align-items:center;color:var(--white);font-weight:700;font-size:15px;width:110px}
.tool svg{width:34px;height:34px;margin-bottom:5px}
.search{height:52px;background:var(--orange);display:flex;align-items:center;padding-left:20px;gap:16px;color:var(--white);font-size:17px}
.search-field{width:194px;height:26px;background:var(--white);border:1px solid #ccc}
.search-btn{width:110px;height:30px;border-radius:3px;background:linear-gradient(#5fd0ff,#179ee6);color:var(--white);font-size:15px;display:flex;align-items:center;justify-content:center;gap:8px}

.main{position:absolute;left:0;top:228px;width:1200px;height:472px;background:linear-gradient(var(--main-blue-light),var(--main-blue))}

.menu{position:absolute;left:10px;top:12px;width:208px;height:430px;border:1px solid #a8dcf6;border-radius:3px;background:linear-gradient(#6cc2ef,#40a6e0);padding:0 6px}
.menu h2{font-family:"Roboto Condensed",Arial,sans-serif;color:var(--white);font-size:25px;font-weight:700;padding:12px 6px 6px}
.menu ul{list-style:none}
.menu li{height:30px;margin-bottom:2px;display:flex;align-items:center;justify-content:space-between;padding:0 12px 0 18px;font-weight:700;font-size:14px;color:var(--white);background:linear-gradient(var(--menu-btn-top),var(--menu-btn-bottom));border:1px solid #8bd6f9}
.menu li.open{background:linear-gradient(#3fb3ec,#0f86cc);color:var(--ink)}
.menu li.sub{background:linear-gradient(var(--sub-btn-top),var(--sub-btn-bottom));color:var(--ink);padding-left:60px;border-color:#b8c2aa}
.menu li svg{width:10px;height:12px}

.content{position:absolute;left:236px;top:0;width:958px;height:450px}
.content h1{font-family:"Roboto Condensed",Arial,sans-serif;color:var(--white);font-size:25px;font-weight:700;position:absolute;left:4px;top:22px}
.panel{position:absolute;left:0;top:60px;width:958px;height:390px;background:var(--panel-blue);border:1px solid var(--panel-edge)}
.back{position:absolute;left:12px;top:7px;width:108px;height:40px;border-radius:3px;background:linear-gradient(#3db4ee,#0e83c8);display:flex;align-items:center;gap:12px;padding-left:8px;color:var(--white);font-weight:700;font-size:17px}
.back svg{width:28px;height:28px}
.course{position:absolute;left:142px;top:18px;font-size:15px;color:var(--ink)}
.term{position:absolute;left:716px;top:20px;font-size:14px;line-height:19px;font-weight:700;color:var(--ink)}
.term span{display:block;color:var(--link);font-weight:400}

.sheet{position:absolute;left:12px;top:68px;width:930px;height:310px;background:var(--white)}
table{width:100%;border-collapse:collapse;font-size:14px}
th{height:38px;background:linear-gradient(#f03a1d,#c81b07);color:var(--white);font-weight:700;font-size:15px;text-align:left;border-bottom:3px solid #a31403}
th.c-assign{padding-left:8px;width:104px}
th.c-desc{padding-left:36px;width:562px}
th.c-dead{padding-left:72px;width:171px}
th.c-mark{padding-left:24px}
td{height:30px;border-right:1px solid #7fc4e6}
tr.odd td{background:var(--row-a)}
tr.even td{background:var(--row-b)}
td.assign{padding-left:12px}
td.assign a{color:var(--link);font-weight:700;text-decoration:underline}
td.desc{padding-left:12px;color:var(--ink)}
td.dead{text-align:center;color:var(--deadline);font-weight:700}
td.dead.plain{font-weight:400}

.footer{position:absolute;left:0;top:700px;width:1200px;height:70px;background:linear-gradient(var(--footer),var(--footer-dark));border-top:2px solid #6f7a7e}
.copy{position:absolute;left:354px;top:27px;color:var(--white);font-size:13px}
.footer-brand{position:absolute;left:600px;top:16px;display:flex;align-items:center;gap:8px;font-weight:700;font-size:30px;color:var(--brand-soft)}
.footer-brand i{width:24px;height:24px;border-radius:50%;background:var(--brand-soft);display:block}
</style>
</head>
<body>

<header class="topbar">
  <div class="app mail">
    <svg viewBox="0 0 38 38"><rect x="4" y="6" width="30" height="26" rx="3" fill="#ffd34d" stroke="#c98a00" stroke-width="1.5"/><rect x="9" y="12" width="20" height="3" fill="#c98a00"/><rect x="9" y="18" width="20" height="3" fill="#c98a00"/><rect x="9" y="24" width="13" height="3" fill="#c98a00"/></svg>Pluxo</div>
  <div class="app calendar">
    <svg viewBox="0 0 38 38"><rect x="4" y="5" width="30" height="30" rx="2" fill="#fff" stroke="#888"/><rect x="4" y="5" width="30" height="8" fill="#3a9a3a"/><text x="19" y="30" text-anchor="middle" font-size="15" font-weight="700" font-family="Arial,sans-serif" fill="#333">14</text></svg>Calender</div>
  <div class="app docs">
    <svg viewBox="0 0 38 38"><rect x="9" y="3" width="9" height="32" fill="#3a6ea8"/><rect x="18" y="6" width="9" height="29" fill="#b53b2d"/><rect x="13" y="9" width="7" height="26" fill="#e0a030"/></svg>Documents</div>
  <div class="app sites">
    <svg viewBox="0 0 38 38"><rect x="3" y="15" width="32" height="18" rx="2" fill="#e8eef2" stroke="#999"/><circle cx="19" cy="15" r="10" fill="#4caf50" stroke="#2d6f30"/></svg>Sites</div>
  <div class="app chat">
    <svg viewBox="0 0 38 38"><ellipse cx="16" cy="15" rx="13" ry="9" fill="#8fd14f"/><ellipse cx="23" cy="24" rx="12" ry="8" fill="#f5a3c7"/></svg>Chat</div>
  <p class="welcome">welcome <span>student@lms.brightnest.nl</span></p>
</header>

<section class="header">
  <div class="brand"><i></i>brightnest</div>
</section>

<aside class="tools">
  <div class="tools-row">
    <div class="tool">
      <svg viewBox="0 0 34 34"><circle cx="17" cy="17" r="13" fill="#f7a21b" stroke="#e06d0a" stroke-width="4" stroke-dasharray="4 3"/><circle cx="17" cy="17" r="5" fill="#c8120c"/></svg>Settings</div>
    <div class="tool">
      <svg viewBox="0 0 34 34"><circle cx="17" cy="17" r="15" fill="#2a8ad6" stroke="#fff" stroke-width="1.5"/><text x="17" y="24" text-anchor="middle" font-size="20" font-weight="700" font-family="Arial,sans-serif" fill="#fff">?</text></svg>Help</div>
    <div class="tool">
      <svg viewBox="0 0 34 34"><circle cx="17" cy="17" r="15" fill="#f7a21b"/><path d="M11 12 A8 8 0 1 0 23 12" fill="none" stroke="#fff" stroke-width="3"/><line x1="17" y1="8" x2="17" y2="17" stroke="#fff" stroke-width="3"/></svg>Sign out</div>
  </div>
  <div class="search">Search
    <div class="search-field"></div>
    <div class="search-btn">Search
      <svg width="18" height="18" viewBox="0 0 18 18"><circle cx="10" cy="7" r="5" fill="none" stroke="#fff" stroke-width="2"/><line x1="6" y1="11" x2="2" y2="16" stroke="#fff" stroke-width="3"/></svg>
    </div>
  </div>
</aside>

<main class="main">
  <nav class="menu">
    <h2>Menu</h2>
    <ul>
      <li>Home<svg viewBox="0 0 10 12"><path d="M1 0 L9 6 L1 12Z" fill="#fff"/></svg></li>
      <li class="open">Study Guide<svg viewBox="0 0 10 12"><path d="M0 3 L10 3 L5 10Z" fill="#fff"/></svg></li>
      <li class="sub">German</li>
      <li class="sub">English</li>
      <li class="sub">French</li>
      <li class="sub">Economics</li>
      <li class="sub">Dutch</li>
      <li class="sub">Chemistry</li>
      <li>Books<svg viewBox="0 0 10 12"><path d="M1 0 L9 6 L1 12Z" fill="#fff"/></svg></li>
      <li>Tests<svg viewBox="0 0 10 12"><path d="M1 0 L9 6 L1 12Z" fill="#fff"/></svg></li>
      <li>Results<svg viewBox="0 0 10 12"><path d="M1 0 L9 6 L1 12Z" fill="#fff"/></svg></li>
    </ul>
  </nav>

  <section class="content">
    <h1>Study Guide Engels</h1>
    <div class="panel">
      <div class="back">
        <svg viewBox="0 0 28 28"><circle cx="14" cy="14" r="12" fill="#fff"/><path d="M20 14 H9 M13 9 L8 14 L13 19" fill="none" stroke="#1a8fd6" stroke-width="3"/></svg>Back</div>
      <p class="course">Engels door leraar@lms.brightnest.nl voor m2@lms.brightnest.nl</p>
      <p class="term">English by Brightnest<span>Eerste trimester (22-12-2010)</span></p>
      <div class="sheet">
        <table>
          <thead>
            <tr><th class="c-assign">Assignment</th><th class="c-desc">Description</th><th class="c-dead">Deadline</th><th class="c-mark">Mark</th></tr>
          </thead>
          <tbody>
            <tr class="odd"><td class="assign"><a>Opdracht 1</a></td><td class="desc">Engels opdracht 1 door leraar@lms.brightnest.nl voor m2@lms.brightnest.nl</td><td class="dead plain">22-12-2010</td><td></td></tr>
            <tr class="even"><td class="assign"><a>Opdracht 2</a></td><td class="desc">Engels opdracht 2 door leraar@lms.brightnest.nl voor m2@lms.brightnest.nl</td><td class="dead">22-12-2010</td><td></td></tr>
            <tr class="odd"><td class="assign"><a>Opdracht 3</a></td><td class="desc">Engels opdracht 3 door leraar@lms.brightnest.nl voor m2@lms.brightnest.nl</td><td class="dead">22-12-2010</td><td></td></tr>
          </tbody>
        </table>
      </div>
    </div>
  </section>
</main>

<footer class="footer">
  <p class="copy">Copyright © 2010-2010 Brightnest</p>
  <div class="footer-brand"><i></i>brightnest</div>
</footer>

</body>
</html>
```